Law firm business card

Information:

Me Marisa Delacourt

website: velmont-juris.ca
email: marisa@velmont-juris.ca
Phone: 514 372-5106
Fax: 514 372-5107

Address:
Delacourt and associates
2917 Brisebois
Montreal, QC
H3K 2T9

Areas of Expertise:
Franchise Agreements, Financing, Acquisition, Real Estate Development, Commercial Agreements and Corporate Law

Target Market(s)

executives, companie managers

Industry/Entity Type

Business

Colors
f78f20
000000

Requirements
Must have
• Must use the logo, the logo is available here:

https://www.filevault-share.net/sh/qe82kd0pl1m7/BXtr9LmQw3zPaYkN

```html
<!DOCTYPE html>
<html lang="en">
<head>
<meta charset="utf-8">
<title>Delacourt and Associates – Business Card</title>
<link href="https://fonts.googleapis.com/css2?family=Cinzel:wght@400;600&display=swap" rel="stylesheet">
<style>
  :root {
    --brand-orange: #f78f20;
    --deep-orange: #e27812;
    --soft-orange: #fba145;
    --ink: #2b2b2b;
    --paper-top: #ffffff;
    --paper-bottom: #e6e6e6;
    --canvas: #ffffff;
  }
  * { box-sizing: border-box; margin: 0; padding: 0; }
  html, body {
    width: 1200px; height: 480px; overflow: hidden;
    background: var(--canvas);
    font-family: "Cinzel", "Times New Roman", serif;
  }
  .stage { position: relative; width: 1200px; height: 480px; }

  .card {
    position: absolute; top: 78px; width: 550px; height: 322px;
    overflow: hidden;
    box-shadow: 4px 6px 8px rgba(0, 0, 0, 0.35);
  }
  .card--front {
    left: 38px;
    background: linear-gradient(180deg, var(--paper-top) 0%, var(--paper-bottom) 100%);
    color: var(--ink);
  }
  .card--back { left: 622px; }

  .firm-mark {
    position: absolute; left: 180px; top: 36px;
    display: flex; align-items: center; gap: 12px;
  }
  .firm-mark__dot {
    width: 48px; height: 48px; border-radius: 50%;
    border: 3px solid var(--brand-orange);
  }
  .firm-mark__rule { width: 1px; height: 54px; background: var(--ink); }
  .firm-mark__name { color: var(--brand-orange); font-weight: 400; line-height: 1; }
  .firm-mark__name .line-1 { display: block; font-size: 32px; letter-spacing: 0.5px; }
  .firm-mark__name .line-2 { display: block; font-size: 17px; letter-spacing: 1px; margin-top: 4px; }

  .expertise {
    position: absolute; left: 36px; top: 128px; width: 500px;
    font-size: 11.5px; font-weight: 600; line-height: 1.3; letter-spacing: 0.2px;
  }

  .lawyer-name {
    position: absolute; left: 266px; top: 168px;
    font-size: 24px; font-weight: 400; color: var(--brand-orange); letter-spacing: 0.5px;
  }
  .office-name {
    position: absolute; left: 36px; top: 214px;
    font-size: 12.5px; font-weight: 600; color: var(--brand-orange);
  }
  .mail-icon { position: absolute; left: 34px; top: 236px; width: 34px; height: 34px; }

  .address, .contact {
    position: absolute;
    font-size: 12px; line-height: 19px; letter-spacing: 0.2px; font-style: normal;
  }
  .address { left: 80px; top: 236px; }
  .contact { left: 266px; top: 218px; }

  .back-field {
    position: absolute; inset: 0;
    background: radial-gradient(ellipse at 50% 45%, var(--soft-orange) 0%, var(--brand-orange) 55%, var(--deep-orange) 100%);
  }
  .back-name {
    position: absolute; inset: 0;
    display: flex; align-items: center; justify-content: center;
    color: var(--deep-orange); font-size: 26px; font-weight: 400; letter-spacing: 1px;
  }
</style>
</head>
<body>
<main class="stage">

  <section class="card card--front" aria-label="Card front">
    <div class="firm-mark">
      <span class="firm-mark__dot" aria-hidden="true"></span>
      <span class="firm-mark__rule" aria-hidden="true"></span>
      <span class="firm-mark__name">
        <span class="line-1">DELACOURT</span>
        <span class="line-2">&amp; ASSOCIATES</span>
      </span>
    </div>

    <p class="expertise">Franchise agreements, financing, acquisition, real estate development, commercial agreements and corporate law</p>

    <h1 class="lawyer-name">Marisa Delacourt</h1>

    <h2 class="office-name">Delacourt and Associates</h2>

    <svg class="mail-icon" viewBox="0 0 34 34" aria-hidden="true">
      <circle cx="17" cy="17" r="15.5" fill="none" stroke="var(--brand-orange)" stroke-width="2"/>
      <rect x="8" y="11" width="18" height="12" rx="1.5" fill="var(--brand-orange)"/>
      <path d="M8.5 11.8 L17 18 L25.5 11.8" fill="none" stroke="#ffffff" stroke-width="1.4"/>
    </svg>

    <address class="address">
      2917 Brisebois<br>
      Montreal, QC<br>
      H3K 2T9
    </address>

    <div class="contact">
      Website: velmont-juris.ca<br>
      Email: marisa@velmont-juris.ca<br>
      Phone: 514 372-5106<br>
      Fax: 514 372-5107
    </div>
  </section>

  <section class="card card--back" aria-label="Card back">
    <div class="back-field" role="img" aria-label="Orange background with flowing decorative line pattern"></div>
    <p class="back-name">DELACOURT</p>
  </section>

</main>
</body>
</html>
```